Website For Custom Home Builder

-Very elegant and simple design as I am a high end custom home builder.
-I build homes $2 million to $10 million range so the website needs to reflect the level of home that I build.
-Attached are photos of homes I have built to use as well as my logo.
-I need final design to be in layered format so my local guy can edit if he needs to.

3 Page Design
1. HomePage:
-logo, some photos,
-“Building beautiful custom homes in Indianapolis for over 20 years”
2. AboutPage:
-Wade Holloran has been building stunning custom homes in the Indianpolis area for over 20 years. As a small boutique building company we only build a handful of homes a year in order to offer our clients the personal attention that their homes deserve. It's this attention to detail that makes our client experience and final product something special and unique.
- family photo
3. ContactPage:
-office photo
-317-552-7190
-wade@whcrafted.com
-415 North Fernmill Rd, Suite 308, Carmel IN 46033

Target Market(s)

Very high end clients looking to build $2 million to $10 million homes.

Industry/Entity Type

Residential high end custom home builder/construction

Coding

Coded - Design and coding required

Number of Pages Required

3 page

Requirements
Must have
• Very simple and elegant design that represents the high end homes that I build.
Nice to have
Should not have
• Should NOT have a lot of clutter or be a very busy page from a design perspective.

```html
<!DOCTYPE html>
<html lang="en">
<head>
<meta charset="utf-8">
<title>Wade Holloran Custom Homes</title>
<link rel="stylesheet" href="https://fonts.googleapis.com/css2?family=Jost:wght@400;500;600&display=swap">
<style>
  :root {
    --ink: #0d0d0d;
    --accent: #f47a1f;
    --button: #ec7a30;
    --page: #efefef;
    --page-shade: #e4e4e4;
    --footer: #d9d9d9;
    --white: #ffffff;
  }
  * { margin: 0; padding: 0; box-sizing: border-box; }
  html, body { width: 1200px; height: 688px; overflow: hidden; }
  body { font-family: "Jost", sans-serif; color: var(--ink); background: var(--page); position: relative; }

  .hero-backdrop {
    position: absolute; left: 0; top: 0; width: 1200px; height: 622px;
    background:
      linear-gradient(90deg, rgba(255,255,255,0.25) 0%, rgba(255,255,255,0) 60%),
      linear-gradient(180deg, var(--page) 0%, var(--page-shade) 55%, var(--page) 100%);
  }

  .site-header { position: absolute; left: 0; top: 0; width: 1200px; height: 100px; }
  .brand {
    position: absolute; left: 67px; top: 34px;
    display: flex; align-items: center; gap: 10px;
    font-size: 19px; font-weight: 500; letter-spacing: 0.5px; color: var(--ink);
  }
  .brand-mark { width: 14px; height: 14px; background: var(--accent); }
  .main-nav { position: absolute; top: 38px; right: 66px; display: flex; gap: 50px; }
  .main-nav a { font-size: 15px; font-weight: 400; color: var(--ink); text-decoration: none; letter-spacing: 0.2px; }
  .main-nav a.is-active { color: var(--accent); font-weight: 500; }

  .hero-copy { position: absolute; left: 67px; top: 213px; }
  .hero-kicker { font-size: 14.5px; font-weight: 600; letter-spacing: 0.3px; }
  .hero-title { font-size: 57px; font-weight: 600; line-height: 1; margin-top: 11px; letter-spacing: 0.5px; }
  .hero-sub { font-size: 17px; font-weight: 600; margin-top: 11px; letter-spacing: 0.2px; }
  .highlight { color: var(--accent); }
  .cta {
    position: absolute; left: 68px; top: 357px; width: 143px; height: 47px;
    background: var(--button); color: var(--white); border-radius: 2px;
    display: flex; align-items: center; justify-content: center;
    font-size: 14px; font-weight: 500; letter-spacing: 0.3px; text-decoration: none;
  }

  .hero-photo { position: absolute; left: 552px; top: 113px; width: 506px; height: 492px; }

  .site-footer {
    position: absolute; left: 0; top: 622px; width: 1200px; height: 66px;
    background: var(--footer); display: flex; align-items: center; justify-content: center;
    font-size: 13.5px; letter-spacing: 0.2px;
  }
</style>
</head>
<body>
  <div class="hero-backdrop" role="img" aria-label="Faded photo of a modern custom home exterior"></div>

  <header class="site-header">
    <div class="brand"><span class="brand-mark"></span>WADE HOLLORAN</div>
    <nav class="main-nav">
      <a href="#" class="is-active">HOME</a>
      <a href="#">ABOUT US</a>
      <a href="#">CONTACT US</a>
    </nav>
  </header>

  <section class="hero-copy">
    <p class="hero-kicker">BUILDING BEAUTIFUL</p>
    <h1 class="hero-title">CUSTOM <span class="highlight">HOMES</span></h1>
    <p class="hero-sub">IN INDIANAPOLIS FOR OVER <span class="highlight">20 YEARS</span></p>
  </section>
  <a class="cta" href="#">GET STARTED</a>

  <svg class="hero-photo" viewBox="0 0 506 492" role="img" aria-label="Photo of a home office with a tall window, wooden desk and leather chair">
    <defs>
      <linearGradient id="room-tones" x1="0" y1="0" x2="1" y2="1">
        <stop offset="0" stop-color="#3a3a3a"/>
        <stop offset="0.35" stop-color="#6f8f5a"/>
        <stop offset="0.55" stop-color="#a8b89a"/>
        <stop offset="0.75" stop-color="#7a4a28"/>
        <stop offset="1" stop-color="#5a5a5a"/>
      </linearGradient>
    </defs>
    <path fill="url(#room-tones)" d="M170 6 C250 -6 380 8 430 80 C470 140 455 200 485 270 C520 360 450 460 310 488 C180 505 80 480 30 410 C-5 350 0 250 30 170 C60 95 100 20 170 6 Z"/>
  </svg>

  <footer class="site-footer">COPYRIGHT © 2023 WADE HOLLORAN. ALL RIGHTS RESERVED.</footer>
</body>
</html>
```